Tranquil Pathway Business Card

Logo attached. (will be printing onto thick white/off white textured card)

Double sided business card for two Therapists working at Tranquil Pathway.

Require one design, but with different name and mobile numbers on each card.

Target Market(s)

Medical, Health

Industry/Entity Type

Business

Contact Information for Business Card

Need one business card design, but a separate card for each person - Colin Marchetti and Marieke de Boeckx.

FRONT OF CARD

Logo

Name (Colin Marchetti on one card, Marieke de Boeckx on the other)
Professional Clinical Hypnotherapist

Consulting Rooms (Near Lindqvist Hospital)
482 Brackenfield Road
Dunmore VIC 3987

Colin@TranquilPathway.example.au OR Marieke@TranquilPathway.example.au

Mobile: 0455 872 604 (for Colin) OR
Mobile: 0467 290 518 (for Marieke)

BACK OF CARD

Logo

Website: www.TranquilPathway.example.au

Phone: 1300 958 471

Requirements
Must have
• Text and logo only. No additiional graphics.

```html
<!DOCTYPE html>
<html lang="en">
<head>
<meta charset="utf-8">
<title>Tranquil Pathway Business Card</title>
<link href="https://fonts.googleapis.com/css2?family=Arimo:wght@400;700&display=swap" rel="stylesheet">
<style>
  :root {
    --navy: #1e2759;
    --slate: #5f605f;
    --ring: #6f706f;
    --paper: #ffffff;
    --backdrop: #ececec;
  }
  html, body {
    margin: 0;
    padding: 0;
    overflow: hidden;
  }
  body {
    width: 1200px;
    height: 924px;
    background: var(--backdrop);
    font-family: "Arimo", Arial, sans-serif;
    position: relative;
  }
  .card {
    position: absolute;
    top: 308px;
    width: 540px;
    height: 309px;
    background: var(--slate);
    overflow: hidden;
    box-shadow: 0 4px 14px rgba(0,0,0,0.18);
  }
  .card--front { left: 40px; }
  .card--back { left: 620px; }
  .card__corner {
    position: absolute;
    inset: 0;
  }
  .brand {
    position: absolute;
    left: 30px;
    top: 30px;
    width: 250px;
    height: 250px;
  }
  .brand__disc {
    position: absolute;
    inset: 0;
    border-radius: 50%;
    background: var(--navy);
    box-shadow: 0 0 0 12px var(--ring);
  }
  .brand__name {
    position: absolute;
    inset: 0;
    display: flex;
    align-items: center;
    justify-content: center;
    text-align: center;
    color: var(--paper);
    font-weight: 700;
    font-size: 30px;
    line-height: 1.15;
  }
  .details {
    position: absolute;
    left: 300px;
    right: 14px;
    top: 0;
    bottom: 0;
    display: flex;
    flex-direction: column;
    align-items: center;
    justify-content: center;
    text-align: center;
    color: var(--paper);
  }
  .details__name {
    font-weight: 700;
    font-size: 22px;
    font-variant: small-caps;
    letter-spacing: 0.5px;
    margin: 0;
  }
  .details__title {
    color: var(--navy);
    font-weight: 700;
    font-size: 11px;
    font-variant: small-caps;
    letter-spacing: 0.4px;
    margin: 2px 0 14px;
  }
  .contact {
    display: flex;
    flex-direction: column;
    align-items: center;
    margin-bottom: 8px;
    font-size: 11px;
    line-height: 1.35;
  }
  .contact__icon {
    width: 18px;
    height: 18px;
    margin-bottom: 3px;
  }
  .contact--large { font-size: 13px; }
</style>
</head>
<body>

<section class="card card--front" aria-label="Card front">
  <svg class="card__corner" viewBox="0 0 540 309" aria-hidden="true">
    <polygon points="0,0 170,0 0,230" fill="var(--navy)"/>
  </svg>
  <div class="brand">
    <div class="brand__disc"></div>
    <div class="brand__name">Tranquil<br>Pathway</div>
  </div>
  <div class="details">
    <h1 class="details__name">Colin Marchetti</h1>
    <p class="details__title">Professional Clinical Hypnotherapist</p>
    <div class="contact">
      <svg class="contact__icon" viewBox="0 0 20 20" aria-hidden="true">
        <circle cx="10" cy="10" r="10" fill="var(--navy)"/>
        <path d="M10 4.5a3.5 3.5 0 0 0-3.5 3.5c0 2.6 3.5 7 3.5 7s3.5-4.4 3.5-7A3.5 3.5 0 0 0 10 4.5z" fill="var(--slate)"/>
        <circle cx="10" cy="8" r="1.3" fill="var(--navy)"/>
      </svg>
      <span>Consulting Rooms (Near Lindqvist Hospital)</span>
      <span>482 Brackenfield Road</span>
      <span>Dunmore VIC 3987</span>
    </div>
    <div class="contact">
      <svg class="contact__icon" viewBox="0 0 20 20" aria-hidden="true">
        <circle cx="10" cy="10" r="10" fill="var(--navy)"/>
        <path d="M7 5l2 2.5-1.2 1.3c.8 1.6 1.8 2.6 3.4 3.4L12.5 11 15 13l-1 2c-4.5-.3-8.3-4.1-8.6-8.6z" fill="var(--slate)"/>
      </svg>
      <span>0455 872 604</span>
    </div>
    <div class="contact">
      <svg class="contact__icon" viewBox="0 0 20 20" aria-hidden="true">
        <circle cx="10" cy="10" r="10" fill="var(--navy)"/>
        <rect x="5" y="6.5" width="10" height="7" fill="var(--slate)"/>
        <path d="M5 6.5l5 4 5-4" fill="none" stroke="var(--navy)" stroke-width="1"/>
      </svg>
      <span>Colin@TranquilPathway.example.au</span>
    </div>
  </div>
</section>

<section class="card card--back" aria-label="Card back">
  <svg class="card__corner" viewBox="0 0 540 309" aria-hidden="true">
    <polygon points="0,0 170,0 0,230" fill="var(--navy)"/>
  </svg>
  <div class="brand">
    <div class="brand__disc"></div>
    <div class="brand__name">Tranquil<br>Pathway</div>
  </div>
  <div class="details">
    <div class="contact contact--large">
      <svg class="contact__icon" viewBox="0 0 20 20" aria-hidden="true">
        <circle cx="10" cy="10" r="10" fill="var(--navy)"/>
        <circle cx="10" cy="10" r="5.5" fill="none" stroke="var(--slate)" stroke-width="1.2"/>
        <ellipse cx="10" cy="10" rx="2.4" ry="5.5" fill="none" stroke="var(--slate)" stroke-width="1"/>
        <line x1="4.5" y1="10" x2="15.5" y2="10" stroke="var(--slate)" stroke-width="1"/>
      </svg>
      <span>www.TranquilPathway.example.au</span>
    </div>
    <div class="contact contact--large">
      <svg class="contact__icon" viewBox="0 0 20 20" aria-hidden="true">
        <circle cx="10" cy="10" r="10" fill="var(--navy)"/>
        <path d="M7 5l2 2.5-1.2 1.3c.8 1.6 1.8 2.6 3.4 3.4L12.5 11 15 13l-1 2c-4.5-.3-8.3-4.1-8.6-8.6z" fill="var(--slate)"/>
      </svg>
      <span>1300 958 471</span>
    </div>
  </div>
</section>

</body>
</html>
```